Web site for Tree Removal Company

What we are looking for:
-------------------------------
Looking for a wordpress web site, you can provide your own template or we can supply you with one (http://pelorin.vextura.com).

What we do
---------------
To see what we do please go to google Australia and google "Tree removal Sydney" or "Tree Removal Melbourne".

Web site requirements
-----------------------------
We prefer you to use our template as it has all our requirements in already.
- Responsive.
- Based on Wordpress.
- Full complaint and compatible with plugs.

Look, Feel and Appearance
------------------------------------
Please use the logo (see attached), for colour scheme, look and feel of the web site.

Thank you for your time and effort!

Target Market(s)

Tree Removal for Residential Homes

Industry/Entity Type

It Company

Number of Pages Required

4 page

Font styles to use
Serif
Sans Serif

Requirements
Must have
• Wordpress
Nice to have
• Original artwork, images and text
Should not have
• non related images or wording

```html
<!DOCTYPE html>
<html lang="en">
<head>
<meta charset="utf-8">
<title>Arbor Kin – Tree Services</title>
<link href="https://fonts.googleapis.com/css2?family=Raleway:ital,wght@0,400;0,500;0,600;0,700;1,400&family=Roboto:ital,wght@0,400;0,500;0,700;1,400&display=swap" rel="stylesheet">
<style>
:root{
  --black:#000;
  --green:#1e8a45;
  --green-tile:#2d775a;
  --green-text:#2e8a5c;
  --lime:#a7c934;
  --ink:#111;
  --body:#555;
  --grey-band:#ebebeb;
  --footer:#2b2b2b;
  --footer-base:#1f1f1f;
  --footer-text:#a9a9a9;
  --white:#fff;
}
*{margin:0;padding:0;box-sizing:border-box}
html,body{width:1200px;height:2308px;overflow:hidden}
body{position:relative;background:var(--white);font-family:'Roboto',Arial,sans-serif;color:var(--body)}
.abs{position:absolute}

/* header */
.site-header{left:0;top:0;width:1200px;height:132px;background:var(--black)}
.brand{left:88px;top:30px;display:flex;flex-direction:column;align-items:center;gap:8px;width:100px}
.brand-dot{width:50px;height:50px;border-radius:50%;background:var(--green-tile)}
.brand-name{font-family:'Raleway',sans-serif;font-weight:600;font-size:14px;letter-spacing:2px;color:#cfcfcf;white-space:nowrap}
.header-phone{right:88px;top:38px;display:flex;align-items:center;gap:8px;font-family:'Roboto',sans-serif;font-weight:500;font-size:27px;color:var(--lime)}
.main-nav{right:88px;top:92px;display:flex}
.main-nav a{font-family:'Roboto',sans-serif;font-weight:700;font-size:12.5px;color:var(--white);text-decoration:none;padding:0 16px;border-left:1px solid #333;line-height:16px}
.main-nav a:first-child{border-left:none}
.main-nav a:last-child{padding-right:0}

/* hero */
.hero{left:0;top:132px;width:1200px;height:430px;background:linear-gradient(120deg,#3d5a2a 0%,#6c8a45 35%,#8c7c5a 55%,#4e6b34 80%,#2f4a22 100%)}
.hero-panel{left:794px;top:247px;width:318px;height:199px;background:rgba(0,0,0,.78);text-align:right;padding:22px 50px 0 0}
.hero-panel p{font-family:'Raleway',sans-serif;font-size:23px;line-height:33px;color:var(--white);font-weight:400}
.hero-panel b{font-weight:700}
.btn-quote{position:absolute;left:51px;top:132px;width:217px;height:41px;background:var(--green);color:var(--white);font-family:'Raleway',sans-serif;font-weight:700;font-size:17px;display:flex;align-items:center;justify-content:center;gap:8px;border-radius:2px}

/* sections */
.section-title{width:1200px;left:0;text-align:center;font-family:'Roboto',sans-serif;font-weight:700;font-size:22px;color:var(--ink)}
.welcome-text{left:88px;top:625px;width:1024px;text-align:center;font-size:14px;line-height:25.5px;color:var(--body)}
.divider{left:88px;top:743px;width:1024px;height:1px;background:#e2e2e2}

.service{width:331px;height:194px}
.service-photo{width:100%;height:155px}
.service-label{height:39px;background:var(--green-tile);color:var(--white);font-family:'Raleway',sans-serif;font-weight:600;font-size:19px;line-height:39px;padding-left:18px}

.reason{width:240px;text-align:center}
.reason svg{display:block;margin:0 auto}
.reason h3{margin-top:14px;font-family:'Raleway',sans-serif;font-weight:700;font-size:20px;color:var(--green-text)}
.reason p{margin-top:6px;font-size:13.5px;line-height:25px;color:var(--body)}

.testimonials-band{left:0;top:1549px;width:1200px;height:345px;background:var(--grey-band)}
.testimonial{width:324px;height:195px;background:var(--white);padding:20px 22px 0 24px}
.testimonial p{font-style:italic;font-size:13px;line-height:24.5px;color:#333}
.testimonial cite{display:block;margin-top:3px;font-style:normal;font-weight:700;font-size:13px;color:var(--green-text)}
.dots{left:570px;top:1853px;display:flex;gap:5px}
.dots span{width:13px;height:13px;border-radius:50%;background:#777}
.dots span:first-child{background:#333}

.cta-band{left:0;top:1894px;width:1200px;height:115px;background:var(--green);display:flex;align-items:center;justify-content:center;font-family:'Raleway',sans-serif;font-weight:700;font-size:29px;color:var(--white)}
.cta-band .hl{color:var(--lime);margin:0 8px}
.cta-band .light{font-weight:400}

.site-footer{left:0;top:2009px;width:1200px;height:238px;background:var(--footer)}
.footer-col{top:31px}
.footer-col h4{font-family:'Roboto',sans-serif;font-weight:700;font-size:13px;color:var(--white);margin-bottom:7px}
.footer-col li{list-style:none;font-size:12.5px;line-height:25px;color:var(--footer-text)}
.footer-col p{font-size:12.5px;line-height:21px;color:var(--footer-text)}
.newsletter{display:flex;margin-top:12px}
.newsletter span{width:192px;height:34px;background:#4a4a4a;color:#bbb;font-size:11.5px;line-height:34px;padding-left:12px}
.newsletter b{width:77px;height:34px;background:var(--green);color:var(--white);font-size:14px;line-height:34px;text-align:center}
.social li{display:flex;align-items:center;gap:14px;line-height:37px}
.social i{display:block;width:28px;height:28px;border-radius:50%;background:#111}
.footer-base{left:0;top:2247px;width:1200px;height:61px;background:var(--footer-base);text-align:center;font-size:11px;line-height:61px;color:#aaa}
</style>
</head>
<body>

<header class="abs site-header">
  <div class="abs brand"><span class="brand-dot"></span><span class="brand-name">ARBOR KIN</span></div>
  <div class="abs header-phone">
    <svg width="24" height="24" viewBox="0 0 24 24" fill="none" stroke="currentColor" stroke-width="2"><circle cx="12" cy="12" r="10.5"/><path d="M8.5 7.5l2 2-1 1.5c.8 1.6 1.9 2.7 3.5 3.5l1.5-1 2 2-1.3 1.3c-3.8-.4-7.6-4.2-8-8z" fill="currentColor" stroke="none"/></svg>
    1580 314 927
  </div>
  <nav class="abs main-nav">
    <a>HOME</a><a>TESTIMONIALS</a><a>TREE SERVICES</a><a>CONTACT</a><a>PHOTO GALLERY</a><a>BLOG</a>
  </nav>
</header>

<section class="abs hero" role="img" aria-label="Photo of an arborist cutting a tree trunk with an orange chainsaw among green foliage"></section>
<div class="abs hero-panel">
  <p>Quality <b>Work</b>,</p>
  <p>Quick Response</p>
  <p>Reasonable <b>Rates</b></p>
  <div class="btn-quote">GET A QUOTE NOW
    <svg width="17" height="17" viewBox="0 0 18 18" fill="none" stroke="#fff" stroke-width="1.5"><circle cx="9" cy="9" r="7.5"/><path d="M5.5 9.2l2.3 2.3 4.7-4.8"/></svg>
  </div>
</div>

<h2 class="abs section-title" style="top:584px">Welcome to Arbor Kin</h2>
<p class="abs welcome-text">Lorem Ipsum is simply dummy text of the printing and typesetting industry. Lorem Ipsum has been the industry's standard dummy text ever since the 1500s, when an unknown printer took a galley of type and scrambled it to make a type specimen book. It has survived not only five centuries, but also the leap into electronic typesetting, remaining essentially unchanged. It was popularised in the 1960s with the release of Stenvale sheets containing Lorem Ipsum passages, and more recently with desktop publishing software like Folio Setter including versions of Lorem Ipsum.</p>
<div class="abs divider"></div>

<h2 class="abs section-title" style="top:768px">Our Services</h2>

<div class="abs service" style="left:88px;top:818px"><div class="service-photo" role="img" aria-label="Photo of a chainsaw cutting into a tree trunk" style="background:linear-gradient(135deg,#5c6b3a,#8a6a45,#4c5a30)"></div><div class="service-label">Tree Removal</div></div>
<div class="abs service" style="left:434px;top:818px"><div class="service-photo" role="img" aria-label="Photo of a stump grinding machine at work" style="background:linear-gradient(135deg,#3f5a2e,#2f5a8a,#7a6a50)"></div><div class="service-label">Stump Grinding</div></div>
<div class="abs service" style="left:781px;top:818px"><div class="service-photo" role="img" aria-label="Photo of a worker in orange gear clearing branches" style="background:linear-gradient(135deg,#6a6a60,#4e6a3a,#8a8a80)"></div><div class="service-label">Chipping Services</div></div>
<div class="abs service" style="left:88px;top:1031px"><div class="service-photo" role="img" aria-label="Photo of a pruning saw cutting a branch" style="background:linear-gradient(135deg,#8a8270,#5a6a3a,#6a5a48)"></div><div class="service-label">Tree Pruning</div></div>
<div class="abs service" style="left:434px;top:1031px"><div class="service-photo" role="img" aria-label="Photo of a climber trimming a palm tree against blue sky" style="background:linear-gradient(135deg,#3a6ac0,#5a8a3a,#2f5aa8)"></div><div class="service-label">Palm Cleaning</div></div>
<div class="abs service" style="left:781px;top:1031px"><div class="service-photo" role="img" aria-label="Photo of a truck with an orange wood chipper" style="background:linear-gradient(135deg,#7a8a90,#c08a3a,#4a6a3a)"></div><div class="service-label">Arborist Services</div></div>

<h2 class="abs section-title" style="top:1268px">Why choose Arbor Kin Services?</h2>

<div class="abs reason" style="left:80px;top:1345px">
  <svg width="70" height="56" viewBox="0 0 70 56" fill="#6a6a6a"><path d="M4 26l14-14 10 4 8-4 16 6 14-4 2 6-12 6 4 8-12 10-8-2-6 4-8-6-12-6z"/><rect x="50" y="4" width="14" height="14" transform="rotate(35 57 11)"/></svg>
  <h3>Truthful</h3><p>Lorem Ipsum is simply dummy text of the printing and typesetting industry. Lorem Ipsum has been.</p>
</div>
<div class="abs reason" style="left:345px;top:1345px">
  <svg width="70" height="56" viewBox="0 0 70 56" fill="#6a6a6a"><path d="M26 30l-8 24 7-4 5 6 5-16zM44 30l8 24-7-4-5 6-5-16z"/><circle cx="35" cy="20" r="17"/><circle cx="35" cy="20" r="11" fill="#fff"/><path d="M35 12l2.4 5 5.4.6-4 3.6 1.2 5.3L35 23.8l-5 2.7 1.2-5.3-4-3.6 5.4-.6z"/></svg>
  <h3>Reputable</h3><p>Lorem Ipsum is simply dummy text of the printing and typesetting industry. Lorem Ipsum has been.</p>
</div>
<div class="abs reason" style="left:614px;top:1345px">
  <svg width="70" height="56" viewBox="0 0 70 56" fill="#6a6a6a"><circle cx="35" cy="7" r="6"/><rect x="28" y="15" width="14" height="24" rx="3"/><rect x="30" y="38" width="4" height="16"/><rect x="36" y="38" width="4" height="16"/><circle cx="20" cy="12" r="5"/><rect x="14" y="19" width="12" height="20" rx="3"/><rect x="16" y="38" width="3" height="14"/><rect x="21" y="38" width="3" height="14"/><circle cx="50" cy="12" r="5"/><rect x="44" y="19" width="12" height="20" rx="3"/><rect x="46" y="38" width="3" height="14"/><rect x="51" y="38" width="3" height="14"/></svg>
  <h3>Highly Professional</h3><p>Lorem Ipsum is simply dummy text of the printing and typesetting industry. Lorem Ipsum has been.</p>
</div>
<div class="abs reason" style="left:880px;top:1345px">
  <svg width="70" height="56" viewBox="0 0 70 56" fill="none" stroke="#6a6a6a" stroke-width="3"><path d="M28 4h14l-4 10h-6z"/><path d="M32 14c-12 8-16 18-14 28 2 8 30 8 34 0 2-10-2-20-14-28"/><path d="M30 32h10M30 38h10"/></svg>
  <h3>Best Value</h3><p>Lorem Ipsum is simply dummy text of the printing and typesetting industry. Lorem Ipsum has been.</p>
</div>

<section class="abs testimonials-band"></section>
<h2 class="abs section-title" style="top:1583px">Satisfied Customer</h2>
<blockquote class="abs testimonial" style="left:88px;top:1635px"><p>Lorem Ipsum is simply dummy text of the printing and typesetting industry. Lorem Ipsum has been the industry's standard dummy text ever since the 1500s, when an unknown printer took a galley of type and scrambled.</p><cite>Marla,Quinn</cite></blockquote>
<blockquote class="abs testimonial" style="left:438px;top:1635px"><p>Lorem Ipsum is simply dummy text of the printing and typesetting industry. Lorem Ipsum has been the industry's standard dummy text ever since the 1500s, when an unknown printer took a galley of type and scrambled.</p><cite>Marla,Quinn</cite></blockquote>
<blockquote class="abs testimonial" style="left:788px;top:1635px"><p>Lorem Ipsum is simply dummy text of the printing and typesetting industry. Lorem Ipsum has been the industry's standard dummy text ever since the 1500s, when an unknown printer took a galley of type and scrambled.</p><cite>Marla,Quinn</cite></blockquote>
<div class="abs dots"><span></span><span></span><span></span></div>

<section class="abs cta-band">CALL US ON <span class="hl">1580 314 927</span><span class="light">OR</span><span class="hl">GET A QUOTE</span></section>

<footer class="abs site-footer">
  <div class="abs footer-col" style="left:88px"><h4>ABOUT US</h4><ul><li>History</li><li>Careers</li><li>What We Do</li><li>Specials</li><li>Testimonials</li><li>Service Areas</li><li>Contact Us</li></ul></div>
  <div class="abs footer-col" style="left:261px"><h4>OUR SERVICES</h4><ul><li>Tree Removal</li><li>Stump Grinding</li><li>Chipping Services</li><li>Tree Pruning</li><li>Palm Cleaning</li><li>Arborist Services</li></ul></div>
  <div class="abs footer-col" style="left:455px"><h4>CORPORATE OFFICE</h4><ul><li>1580 314 927</li><li>info@arborkin.com</li><li>PO Box 318</li><li>Fairview, PA 2471</li></ul></div>
  <div class="abs footer-col" style="left:686px"><h4>NEWSLETTER SIGNUP</h4><p>Lorem Ipsum is simply dummy text<br>of the printing</p><div class="newsletter"><span>Email Address</span><b>SIGN UP</b></div></div>
  <div class="abs footer-col" style="left:990px"><h4>FOLLOW US</h4><ul class="social"><li><i></i>Grovebook</li><li><i></i>Chirpline</li><li><i></i>Worknet</li><li><i></i>Clipstream</li></ul></div>
</footer>
<div class="abs footer-base">Copyright © 2015 arborkin.com. All Rights Reserved.</div>

</body>
</html>
```